Tolvane Air and Electrical Website

Simple and easy to use website for a Electrical and Air Conditioning contracting business.Use stock photosOnline contact portallogo still to be supplied

Target Market(s)

Mums and Dads who want a local contractor

Coding

Coded - Design and coding required

Number of Pages Required

2 page

Font styles to use
Sans Serif

Colors
f04a50
3276b5
33a6d7

Requirements
Must have
• Simple and easy to use
• Ph number
• 4 web address; linked to page
• 0417385926
• tolvane.com.au
• tolvaneelectrical.com.au
• tolvaneairandelectrical.com.au
• tolvaneair.com.au
Nice to have
• Split System Air Con Picture
• Electrical Pictures

```html
<!DOCTYPE html>
<html lang="en">
<head>
<meta charset="utf-8">
<title>Tolvane Air and Electrical</title>
<link href="https://fonts.googleapis.com/css2?family=Questrial&family=Lato:wght@400;700&display=swap" rel="stylesheet">
<style>
:root{
  --red:#f0262e;
  --blue:#1d70b8;
  --sky:#33a6d7;
  --ink:#222;
  --text:#444;
  --muted:#666;
  --band:#f3f3f3;
  --footer:#2c2c2e;
  --line:#e2e2e2;
}
*{box-sizing:border-box;margin:0;padding:0}
html,body{width:1200px;height:4079px;overflow:hidden;background:#fff}
body{font-family:'Lato',sans-serif;color:var(--text);position:relative}
.abs{position:absolute}
h2,h3,.display{font-family:'Questrial',sans-serif;font-weight:400;color:var(--ink);letter-spacing:2px}
.btn{position:absolute;display:flex;align-items:center;justify-content:center;color:#fff;font-size:14px;background:var(--blue);text-decoration:none}
.btn.red{background:var(--red)}
a{color:inherit}

/* header */
.topbar{position:absolute;left:0;top:0;width:1200px;height:107px}
.call{position:absolute;left:72px;top:42px;display:flex;gap:10px;align-items:center}
.call small{display:block;color:var(--blue);font-size:12px;font-weight:700}
.call strong{display:block;color:var(--red);font-size:14px;font-weight:400;letter-spacing:1px}
.brand{position:absolute;left:500px;top:36px;display:flex;align-items:center;gap:10px}
.brand .mark{width:38px;height:38px;background:var(--red)}
.brand span{font-family:'Questrial',sans-serif;font-size:22px;color:var(--blue);letter-spacing:1px}
.social{position:absolute;display:flex;gap:10px}
.social i{width:24px;height:24px;border:2px solid var(--blue);border-radius:50%;display:block}
.social i:first-child{border-color:var(--red)}
.nav{position:absolute;left:0;top:107px;width:1200px;height:41px;background:var(--blue)}
.nav ul{list-style:none;position:absolute;left:81px;top:0;display:flex;height:41px}
.nav li{height:41px;display:flex;align-items:center;justify-content:center;color:#fff;font-size:14px;border-right:1px solid rgba(255,255,255,.35)}
.nav li.on{background:var(--red);border:none}

/* hero */
.hero{position:absolute;left:0;top:148px;width:1200px;height:442px;background:linear-gradient(90deg,#c9c3bd 0%,#e7e7e7 45%,#eeeeee 100%)}
.hero .photo{position:absolute;left:0;top:0;width:640px;height:442px;background:linear-gradient(100deg,#8e7a68 0%,#c7bdb3 35%,#e9e9e9 70%,#e3e3e3 100%)}
.hero h1{position:absolute;left:712px;top:125px;font-family:'Questrial',sans-serif;font-weight:400;font-size:30px;line-height:38px;color:#222;letter-spacing:2px}
.hero p{position:absolute;left:712px;top:223px;width:420px;font-size:13px;line-height:15px;color:#444}
.dots{position:absolute;left:576px;top:404px;display:flex;gap:6px}
.dots i{width:6px;height:6px;border-radius:50%;background:#555;display:block}
.dots i:first-child{background:var(--sky)}

/* section headings */
.sec-title{position:absolute;left:0;width:1200px;text-align:center;font-size:30px}
/* about */
.about-text{position:absolute;left:230px;top:684px;width:740px;text-align:center;font-size:13.5px;line-height:16px;color:#333}
.feature{position:absolute;top:800px;width:200px;text-align:center}
.feature svg{display:block;margin:0 auto;height:80px}
.feature h3{font-size:19px;line-height:23px;margin-top:12px;letter-spacing:2.5px}
.feature p{font-size:12.5px;line-height:16px;color:#444;margin-top:14px}
.feature .more{display:block;margin-top:14px;font-size:13px;text-decoration:underline;color:#333}

/* services */
.card{position:absolute;width:328px}
.card .pic{width:328px;height:260px}
.card h3{text-align:center;font-size:18px;line-height:23px;letter-spacing:2.5px;margin-top:16px}

/* band */
.band{position:absolute;left:0;top:1965px;width:1193px;height:425px;background:var(--band)}
.band .frame{position:absolute;left:70px;top:42px;width:505px;height:335px;background:#fff;padding:10px}
.band .frame div{width:100%;height:100%;background:linear-gradient(90deg,#3a4a6a 0%,#8a8d93 55%,#e0d8cc 80%,#c98a3a 100%)}
.band h2{position:absolute;left:641px;top:80px;font-size:32px;line-height:38px;letter-spacing:3px}
.band p{position:absolute;left:640px;width:470px;font-size:13px;line-height:16px;color:#444}

/* categories */
.cats{position:absolute;top:2545px;list-style:none}
.cats li{display:flex;align-items:center;gap:22px;height:38.4px;font-family:'Questrial',sans-serif;font-size:19px;color:#333;letter-spacing:1.5px}
.cats svg{width:20px;height:20px;flex:none}

/* blogs */
.blog{position:absolute;top:3045px;width:335px;height:365px;background:#f4f4f4}
.blog .pic{position:absolute;left:12px;top:12px;width:311px;height:208px}
.blog .date{position:absolute;left:90px;top:199px;width:154px;height:37px;background:var(--blue);color:#fff;font-size:14px;display:flex;align-items:center;justify-content:center}
.blog h4{position:absolute;left:25px;top:262px;font-weight:400;font-size:13px;color:#222;letter-spacing:.5px}
.blog p{position:absolute;left:25px;top:287px;width:290px;font-size:12.5px;line-height:15px;color:#555}
.blog .cont{position:absolute;left:25px;top:333px;font-size:11px;color:#444;display:flex;align-items:center;gap:3px}

/* newsletter */
.news-input{position:absolute;left:330px;top:3600px;width:420px;height:43px;background:#f4f4f4;border:1px solid #eee;font-size:13px;font-style:italic;color:#888;padding:14px 20px}

/* footer */
.footer{position:absolute;left:0;top:3680px;width:1200px;height:342px;background:var(--footer);color:#fff}
.footer h5{position:absolute;top:84px;font-family:'Questrial',sans-serif;font-weight:400;font-size:15px;letter-spacing:.5px}
.footer h5::after{content:"";display:block;width:30px;height:2px;background:var(--red);margin-top:8px}
.footer ul{position:absolute;left:390px;top:125px;list-style:none;font-size:13px;line-height:23.5px}
.footer ul li::before{content:"•";margin-right:12px}
.footer .txt{font-size:13px;line-height:23px}
.field{position:absolute;height:27px;background:#3b3b3e;border:1px solid #4a4a4d;font-size:12px;padding:5px 7px;color:#ddd}
.copy{position:absolute;left:80px;top:4046px;font-size:12px;color:#333}
</style>
</head>
<body>

<header class="topbar">
  <div class="call">
    <svg width="32" height="32" viewBox="0 0 32 32" fill="none" stroke="#1d70b8" stroke-width="2.2"><circle cx="16" cy="16" r="14"/><path d="M11 9l3 4-2 2c1 2 3 4 5 5l2-2 4 3-2 3c-6 0-12-6-12-12z"/></svg>
    <div><small>Call Now Fast Service</small><strong>0417385926</strong></div>
  </div>
  <div class="brand"><div class="mark"></div><span>Tolvane Air and Electrical</span></div>
  <div class="social" style="left:958px;top:52px"><i></i><i></i><i></i><i></i><i></i></div>
</header>

<nav class="nav">
  <ul>
    <li class="on" style="width:110px">Home</li>
    <li style="width:140px">About us</li>
    <li style="width:145px">Services</li>
    <li style="width:148px">Categories</li>
    <li style="width:186px">Testimonials</li>
    <li style="width:126px">Blogs</li>
    <li style="width:151px">Contact us</li>
  </ul>
  <svg class="abs" style="left:1105px;top:12px" width="18" height="18" viewBox="0 0 18 18" fill="none" stroke="#fff" stroke-width="2"><circle cx="7.5" cy="7.5" r="5.5"/><path d="M12 12l5 5"/></svg>
</nav>

<section class="hero">
  <div class="photo" role="img" aria-label="Technician servicing a wall-mounted split system air conditioner"></div>
  <h1>Air conditoning Repair &amp;<br>Electrical Service</h1>
  <p>Lorem Ipsum is simply dummy text of the printing and type setting industry. Lorem Ipsum has been the industry's</p>
  <a class="btn" style="left:711px;top:275px;width:153px;height:43px">Read More</a>
  <a class="btn red" style="left:884px;top:275px;width:153px;height:43px">Get A Quote</a>
  <div class="dots"><i></i><i></i><i></i><i></i></div>
  <svg class="abs" style="left:1036px;top:392px" width="86" height="20" viewBox="0 0 86 20" fill="none" stroke-width="2"><path d="M36 10H2M9 3L2 10l7 7" stroke="#333"/><path d="M50 10h34M77 3l7 7-7 7" stroke="#888"/></svg>
</section>

<h2 class="sec-title" style="top:632px">About us</h2>
<p class="about-text">With over 17 years' experience in the Electrical Industry, Tolvane Electrical provides a superior level of knowledge, a broad range of products and a high standard of customer service.</p>
<a class="btn" style="left:520px;top:740px;width:153px;height:41px">Read More</a>

<div class="feature" style="left:76px">
  <svg viewBox="0 0 80 80" width="80" fill="none" stroke="#f0262e" stroke-width="3"><path d="M62 26A28 28 0 1 0 66 50"/><path d="M56 22l7 4 2-8"/><text x="14" y="46" font-size="18" fill="#f0262e" stroke="none" font-family="Lato" font-weight="700">24</text><circle cx="58" cy="54" r="11" fill="#f0262e"/><text x="54" y="60" font-size="15" fill="#fff" stroke="none" font-family="Lato" font-weight="700">7</text></svg>
  <h3>Open 24/7<br>Available</h3>
  <p>Lorem Ipsum is simply dummy of the printing and typesetting in the industry.</p>
  <a class="more">Read More..</a>
</div>
<div class="feature" style="left:363px">
  <svg viewBox="0 0 80 80" width="80" fill="none" stroke="#f0262e" stroke-width="3"><circle cx="40" cy="30" r="22"/><circle cx="40" cy="30" r="14"/><path d="M40 21l3 6 6 1-4 4 1 6-6-3-6 3 1-6-4-4 6-1z"/><path d="M27 48l-6 22 8-4 5 8 6-22M53 48l6 22-8-4-5 8-6-22"/></svg>
  <h3>Quality</h3>
  <p>Lorem Ipsum is simply dummy of the printing and typesetting in the industry.</p>
  <a class="more">Read More..</a>
</div>
<div class="feature" style="left:646px">
  <svg viewBox="0 0 80 80" width="80" fill="none" stroke="#f0262e" stroke-width="3"><path d="M44 8h26v26L34 70 8 44z"/><circle cx="58" cy="20" r="5"/><path d="M22 46l14-14M30 54l14-14"/></svg>
  <h3>Price</h3>
  <p>Lorem Ipsum is simply dummy of the printing and typesetting in the industry.</p>
  <a class="more">Read More..</a>
</div>
<div class="feature" style="left:930px">
  <svg viewBox="0 0 80 80" width="80" fill="none" stroke="#f0262e" stroke-width="3"><path d="M22 30a18 18 0 0 1 36 0z"/><path d="M18 30h44M40 12v8"/><path d="M28 36v6a12 12 0 0 0 24 0v-6"/><path d="M14 78V64c0-8 8-12 14-14l12 10 12-10c6 2 14 6 14 14v14"/><path d="M40 60v18"/></svg>
  <h3>Professionally<br>Technicians</h3>
  <p>Lorem Ipsum is simply dummy of the printing and typesetting in the industry.</p>
  <a class="more">Read More..</a>
</div>

<h2 class="sec-title" style="top:1108px">Service</h2>
<div class="card" style="left:80px;top:1172px"><div class="pic" role="img" aria-label="Row of circuit breakers in a switchboard" style="background:linear-gradient(160deg,#3a3a3a,#cfcfcf 45%,#9a8b55 80%,#2b2b2b)"></div><h3>Domestic</h3></div>
<div class="card" style="left:437px;top:1172px"><div class="pic" role="img" aria-label="Bright open-plan commercial office interior" style="background:linear-gradient(135deg,#e8e6e2,#cfc7bb 60%,#9c8f7e)"></div><h3>Commercial</h3></div>
<div class="card" style="left:791px;top:1172px"><div class="pic" role="img" aria-label="Industrial warehouse with stacked shelving" style="background:linear-gradient(180deg,#6b7680,#9a8466 55%,#4a4f55)"></div><h3>Industrial</h3></div>
<div class="card" style="left:80px;top:1489px"><div class="pic" role="img" aria-label="Installer in a hard hat fitting a split system unit" style="background:linear-gradient(150deg,#f2f2f2 30%,#d9d4cc 60%,#8a5a4a)"></div><h3>Split System<br>Installations</h3></div>
<div class="card" style="left:437px;top:1489px"><div class="pic" role="img" aria-label="Technicians working in a data server room" style="background:linear-gradient(120deg,#2f3a48,#6e7c8c 50%,#1d2630)"></div><h3>Data &amp; Communication<br>Installation</h3></div>
<div class="card" style="left:791px;top:1489px"><div class="pic" role="img" aria-label="Multimeter probes testing an electrical panel" style="background:linear-gradient(135deg,#b45a4a,#d9d9d9 45%,#3a7fb8 85%)"></div><h3>Electrical Testing<br>&amp; Tagging</h3></div>
<a class="btn" style="left:524px;top:1855px;width:154px;height:43px">View More</a>

<section class="band">
  <div class="frame"><div role="img" aria-label="Technician checking air conditioning pressure gauges beside an open unit"></div></div>
  <h2>24hr Breakdown &amp; Repair<br>Service</h2>
  <p style="top:192px">Tolvane Electrical has a qualified electrician standing by with a fully stocked truck to assist you and your electrical needs around the clock.</p>
  <p style="top:257px">24 hour emergency electrical services for your convenience.</p>
  <a class="btn" style="left:637px;top:303px;width:153px;height:43px">Read More</a>
</section>

<h2 class="sec-title" style="top:2440px">Service Categories</h2>
<svg width="0" height="0" style="position:absolute"><defs><symbol id="tick" viewBox="0 0 20 20"><path d="M17 8.5A7.5 7.5 0 1 1 13 3.5" fill="none" stroke="#1d70b8" stroke-width="2"/><path d="M6 10l3.5 3.5L18 4" fill="none" stroke="#1d70b8" stroke-width="2.4"/></symbol></defs></svg>
<ul class="cats" style="left:80px">
  <li><svg><use href="#tick"/></svg>Air Conditioning</li>
  <li><svg><use href="#tick"/></svg>Reverse Cycle</li>
  <li><svg><use href="#tick"/></svg>Split System</li>
  <li><svg><use href="#tick"/></svg>Installation</li>
  <li><svg><use href="#tick"/></svg>Evaporative Cooling</li>
  <li><svg><use href="#tick"/></svg>Repairs &amp; Maintenance</li>
  <li><svg><use href="#tick"/></svg>Ducted</li>
  <li><svg><use href="#tick"/></svg>Air Conditioners</li>
  <li><svg><use href="#tick"/></svg>Appliance Repairs</li>
  <li><svg><use href="#tick"/></svg>Air Conditioners</li>
</ul>
<ul class="cats" style="left:483px">
  <li><svg><use href="#tick"/></svg>Electricians</li>
  <li><svg><use href="#tick"/></svg>Home Entertainment System</li>
  <li><svg><use href="#tick"/></svg>Security Lighting</li>
  <li><svg><use href="#tick"/></svg>Data Cabling</li>
  <li><svg><use href="#tick"/></svg>Safety Switches</li>
  <li><svg><use href="#tick"/></svg>Test &amp; Tag</li>
  <li><svg><use href="#tick"/></svg>Lighting</li>
  <li><svg><use href="#tick"/></svg>Rewiring</li>
  <li><svg><use href="#tick"/></svg>Solar Power</li>
  <li><svg><use href="#tick"/></svg>24/7 Emergency Electricians</li>
</ul>
<ul class="cats" style="left:898px">
  <li><svg><use href="#tick"/></svg>Repairs</li>
  <li><svg><use href="#tick"/></svg>Renovations</li>
  <li><svg><use href="#tick"/></svg>Power Points</li>
  <li><svg><use href="#tick"/></svg>New Installations</li>
  <li><svg><use href="#tick"/></svg>New Homes</li>
  <li><svg><use href="#tick"/></svg>Switchboards</li>
  <li><svg><use href="#tick"/></svg>Hot Water Systems</li>
  <li><svg><use href="#tick"/></svg>Electric</li>
</ul>

<h2 class="sec-title" style="top:2985px">Latest Blogs</h2>
<article class="blog" style="left:68px">
  <div class="pic" role="img" aria-label="Living room with a wall air conditioner above a sofa" style="background:linear-gradient(180deg,#d8d4cf,#b9a998 60%,#8a8278)"></div>
  <div class="date">03 June, 2019</div>
  <h4>What is Lorem Ipsum?</h4>
  <p>Lorem Ipsum is simply dummy &nbsp;the printing a typesetting industry.</p>
  <span class="cont">Continue.. <svg width="11" height="11" viewBox="0 0 12 12" fill="none" stroke="#444"><circle cx="6" cy="6" r="5"/><path d="M5 3.5L7.5 6 5 8.5"/></svg></span>
</article>
<article class="blog" style="left:435px">
  <div class="pic" role="img" aria-label="Technician cleaning an air conditioner filter" style="background:linear-gradient(160deg,#e9e9e9,#c8c8c8 50%,#7d93a8)"></div>
  <div class="date">03 June, 2019</div>
  <h4>What is Lorem Ipsum?</h4>
  <p>Lorem Ipsum is simply dummy &nbsp;the printing a typesetting industry.</p>
  <span class="cont">Continue.. <svg width="11" height="11" viewBox="0 0 12 12" fill="none" stroke="#444"><circle cx="6" cy="6" r="5"/><path d="M5 3.5L7.5 6 5 8.5"/></svg></span>
</article>
<article class="blog" style="left:795px">
  <div class="pic" role="img" aria-label="Hands repairing the circuit board of an appliance" style="background:linear-gradient(135deg,#b44a4a,#d0d0d0 45%,#4f6a55 85%)"></div>
  <div class="date">03 June, 2019</div>
  <h4>What is Lorem Ipsum?</h4>
  <p>Lorem Ipsum is simply dummy &nbsp;the printing a typesetting industry.</p>
  <span class="cont">Continue.. <svg width="11" height="11" viewBox="0 0 12 12" fill="none" stroke="#444"><circle cx="6" cy="6" r="5"/><path d="M5 3.5L7.5 6 5 8.5"/></svg></span>
</article>
<a class="btn" style="left:524px;top:3445px;width:154px;height:43px">View More</a>

<h2 class="sec-title" style="top:3518px;font-size:28px">Join Our Newletter</h2>
<p class="abs" style="left:0;top:3560px;width:1200px;text-align:center;font-size:13px;color:#444">Lorem Ipsum is simply dummy.</p>
<div class="news-input">Email Here</div>
<a class="btn" style="left:760px;top:3600px;width:153px;height:43px">Submit</a>

<footer class="footer">
  <div class="abs" style="left:80px;top:68px;display:flex;align-items:center;gap:10px"><div style="width:34px;height:34px;background:var(--red)"></div><span style="font-family:'Questrial',sans-serif;font-size:19px;color:#fff">Tolvane Air and Electrical</span></div>
  <p class="abs txt" style="left:80px;top:138px;width:240px">Lorem Ipsum is simply dummy text of the printing and typesetting industry has been the industry's</p>
  <span class="abs" style="left:80px;top:222px;font-size:13px;display:flex;align-items:center;gap:5px">Read More.. <svg width="13" height="13" viewBox="0 0 12 12" fill="none" stroke="#fff"><circle cx="6" cy="6" r="5"/><path d="M5 3.5L7.5 6 5 8.5"/></svg></span>

  <h5 style="left:391px">Quick Link</h5>
  <ul><li>Home</li><li>About us</li><li>Services</li><li>Categories</li><li>Testimonials</li><li>Blogs</li><li>Contact us</li></ul>

  <h5 style="left:565px">Quick Contact</h5>
  <svg class="abs" style="left:565px;top:128px" width="12" height="15" viewBox="0 0 12 15" fill="none" stroke="#fff" stroke-width="1.3"><path d="M6 14S1 8.5 1 5.5a5 5 0 0 1 10 0C11 8.5 6 14 6 14z"/><circle cx="6" cy="5.5" r="1.8"/></svg>
  <p class="abs txt" style="left:591px;top:125px">14 Wren Lane,<br>Kelsby East,<br>Victoria 1234</p>
  <svg class="abs" style="left:564px;top:217px" width="14" height="12" viewBox="0 0 14 12" fill="none" stroke="#fff" stroke-width="1.2"><rect x="1" y="3" width="12" height="8" rx="1"/><path d="M3 3V1h8v2M4 6h6M4 8h6"/></svg>
  <p class="abs txt" style="left:591px;top:211px">0417385926</p>
  <svg class="abs" style="left:564px;top:241px" width="14" height="10" viewBox="0 0 14 10" fill="none" stroke="#fff" stroke-width="1.2"><rect x="1" y="1" width="12" height="8"/><path d="M1 1l6 5 6-5"/></svg>
  <p class="abs txt" style="left:591px;top:234px">info@tolvane.com.au</p>

  <h5 style="left:797px">Contact us</h5>
  <div class="field" style="left:797px;top:118px;width:93px">Name</div>
  <div class="field" style="left:897px;top:118px;width:93px">Email</div>
  <div class="field" style="left:995px;top:118px;width:93px">Phone</div>
  <div class="field" style="left:797px;top:151px;width:291px;height:70px">Message</div>
  <a class="btn" style="left:797px;top:237px;width:153px;height:43px">Send</a>
</footer>

<p class="copy">CopyRight©2019 Tolvane. All Right Reserve</p>
<div class="social" style="left:958px;top:4038px"><i></i><i></i><i></i><i></i><i></i></div>

</body>
</html>
```